Flyer Design

MALLOWBYS, fish & Chips . 17 Fennick Lane, Chessington KT4 7RD, TEL; 0208 6142937
This is a existing business of Fish and Chips, would like to use picture of fish & Chips and the menu on the other side

Industry/Entity Type

Business

```html
<!DOCTYPE html>
<html lang="en">
<head>
<meta charset="utf-8">
<title>Mallowbys Fish &amp; Chips Flyer</title>
<link rel="stylesheet" href="https://fonts.googleapis.com/css2?family=Oswald:wght@500;700&family=Exo+2:ital,wght@1,900&display=swap">
<style>
  :root {
    --wood-light: #8a5a36;
    --wood-mid: #74482a;
    --wood-dark: #5e3820;
    --white: #ffffff;
    --yellow: #fff200;
    --green: #8dc63f;
    --photo-gold: #c0772a;
    --photo-cream: #e9dcc4;
    --photo-green: #5e8a3a;
  }
  html, body {
    margin: 0;
    padding: 0;
    overflow: hidden;
    background: #d8d8d8;
  }
  .flyer {
    position: relative;
    width: 900px;
    height: 1200px;
    overflow: hidden;
    font-family: "Oswald", "Arial Narrow", sans-serif;
    color: var(--white);
  }
  .hero-photo {
    position: absolute;
    left: 0;
    top: 0;
    width: 900px;
    height: 570px;
    background:
      radial-gradient(ellipse 260px 140px at 640px 110px, var(--photo-green) 0%, rgba(94,138,58,0) 100%),
      radial-gradient(ellipse 200px 120px at 260px 120px, #e7b45c 0%, rgba(231,180,92,0) 100%),
      radial-gradient(ellipse 320px 170px at 250px 380px, #a85a1c 0%, rgba(168,90,28,0) 100%),
      radial-gradient(ellipse 230px 180px at 720px 350px, #b8661f 0%, rgba(184,102,31,0) 100%),
      linear-gradient(180deg, var(--photo-gold) 0%, #9c5520 55%, var(--photo-cream) 100%);
  }
  .wood-panel {
    position: absolute;
    left: 0;
    top: 0;
    width: 900px;
    height: 1200px;
  }
  .frame {
    position: absolute;
    left: 50px;
    top: 36px;
    width: 798px;
    height: 1120px;
    border: 1.5px solid rgba(255,255,255,0.85);
    box-sizing: border-box;
  }
  .brand-name {
    position: absolute;
    left: 0;
    top: 574px;
    width: 900px;
    margin: 0;
    text-align: center;
    font-family: "Oswald", "Arial Narrow", sans-serif;
    font-weight: 700;
    font-size: 134px;
    line-height: 1;
    letter-spacing: 3px;
  }
  .brand-tagline {
    position: absolute;
    left: 0;
    top: 704px;
    width: 900px;
    margin: 0;
    text-align: center;
    font-family: "Exo 2", sans-serif;
    font-style: italic;
    font-weight: 900;
    font-size: 54px;
    line-height: 1;
    letter-spacing: 3px;
    color: var(--yellow);
  }
  .dish-gallery {
    position: absolute;
    top: 792px;
    left: 0;
    width: 900px;
    height: 155px;
  }
  .dish-photo {
    position: absolute;
    top: 0;
    height: 155px;
    box-sizing: border-box;
    border: 4px solid var(--white);
  }
  .dish-photo.fillet { left: 80px; width: 241px;
    background: radial-gradient(ellipse at 45% 40%, #d59a48 0%, #b8722c 60%, #7fa7b8 100%); }
  .dish-photo.wrapped { left: 332px; width: 245px;
    background: radial-gradient(ellipse at 40% 35%, #f0ebe2 0%, #e0b45a 55%, #d89a3a 100%); }
  .dish-photo.platter { left: 588px; width: 231px;
    background: radial-gradient(ellipse at 60% 40%, #b46a2c 0%, #e4a548 55%, #c88a3a 100%); }
  .promo-line {
    position: absolute;
    left: 0;
    width: 900px;
    margin: 0;
    text-align: center;
    font-weight: 500;
    font-size: 20px;
    line-height: 1;
    letter-spacing: 0.3px;
  }
  .promo-line.offer { top: 966px; }
  .promo-line.call { top: 1007px; }
  .address-band {
    position: absolute;
    left: 50px;
    top: 1056px;
    width: 800px;
    height: 47px;
    background: var(--green);
    display: flex;
    align-items: center;
    justify-content: center;
    font-weight: 500;
    font-size: 19px;
    letter-spacing: 0.3px;
  }
  .phone {
    position: absolute;
    left: 0;
    top: 1116px;
    width: 900px;
    margin: 0;
    text-align: center;
    font-weight: 500;
    font-size: 24px;
    line-height: 1;
    letter-spacing: 0.5px;
  }
</style>
</head>
<body>
<main class="flyer">
  <div class="hero-photo" role="img" aria-label="Two golden battered fish fillets with chips, green salad and a pot of tartare sauce on a white plate"></div>

  <svg class="wood-panel" width="900" height="1200" viewBox="0 0 900 1200" role="img" aria-label="Warm brown wooden board background">
    <defs>
      <linearGradient id="woodTone" x1="0" y1="0" x2="0" y2="1">
        <stop offset="0" stop-color="#8d5c38"/>
        <stop offset="0.5" stop-color="#7a4c2d"/>
        <stop offset="1" stop-color="#5c361e"/>
      </linearGradient>
    </defs>
    <path d="M0 548 C 60 548, 110 520, 180 508 C 300 496, 600 496, 720 508 C 790 516, 840 545, 900 548 L 900 1200 L 0 1200 Z" fill="url(#woodTone)"/>
  </svg>

  <div class="frame"></div>

  <h1 class="brand-name">MALLOWBYS</h1>
  <p class="brand-tagline">FISH &amp; CHIPS</p>

  <div class="dish-gallery">
    <div class="dish-photo fillet" role="img" aria-label="Battered fish fillet with parsley on chips"></div>
    <div class="dish-photo wrapped" role="img" aria-label="Fish and chips served in paper with dip"></div>
    <div class="dish-photo platter" role="img" aria-label="Fried fish with chips and salad on a plate"></div>
  </div>

  <p class="promo-line offer">TRY OUR FAMOUS FISH &amp; CHIPS WITH GARLIC FRIES!</p>
  <p class="promo-line call">CALL NOW FOR RESERVATIONS</p>

  <div class="address-band">17 Fennick Lane, Chessington KT4 7RD</div>
  <p class="phone">Tel: 0208 6142937</p>
</main>
</body>
</html>
```